Business Card - Business Consultancy

Newly Established Company, specializing in Business Consultancy, Human Resource Management, Talent Acquisition and Payroll Solutions.

We need a Business card design which portrays "elegance" and a very sleek yet business-like design. We would like a nice blue trimming (which goes well with the logo) to separate the content of the business card at the top. We would also like to see the design using the color silver either as a background or incorporated into it.

The final design should be a Business card which has colors matching the logo; a nice font; the above-mentioned specifics that adheres to the theme of "a stylish and professional business"

FYI: please do not have too fanciful designs.

Industry/Entity Type

Business Consultant

Contact Information for Business Card

Marcus Tellon
Business Development Director
Brightpath HR Consulting Private Limited
27 Wexford Lane, #05-03B
Harbourview Trade Tower
Singapore 061739
Mobile : (+65) 94386157
Email : mtellon@brightpathhr-advisory.com
Alternative : brightpathhradvisory@mailbox-example.com

Requirements
Must have
• Nice Blue Trimming matching Logo which separates content, see attached
• Design incorporates either a silver background or the use of the color silver
Should not have
• No Fanciful Designs
• No Childish Designs
• No Overly Complicated Designs

```html
<!DOCTYPE html>
<html lang="en">
<head>
<meta charset="utf-8">
<title>Brightpath HR Consulting – Business Card</title>
<link rel="stylesheet" href="https://fonts.googleapis.com/css2?family=Open+Sans:wght@400;700&display=swap">
<style>
  :root {
    --blue: #2a7fc9;
    --blue-deep: #1f63a6;
    --green: #7cc142;
    --ink: #1f1f1f;
    --grey: #6b6b6b;
    --silver-light: #f2f2f2;
    --silver-mid: #bfc2c5;
    --silver-dark: #7d8084;
    --paper: #ffffff;
    --backdrop: #e6e7e9;
  }
  * { box-sizing: border-box; margin: 0; padding: 0; }
  html, body { width: 1200px; height: 900px; overflow: hidden; }
  body {
    background: var(--backdrop);
    font-family: "Open Sans", Arial, sans-serif;
    color: var(--ink);
    position: relative;
  }
  .card {
    position: absolute;
    left: 270px;
    width: 660px;
    height: 378px;
    background: var(--paper);
    box-shadow: 0 10px 30px rgba(0,0,0,0.18);
    overflow: hidden;
  }
  .card--logo { top: 40px; }
  .card--details { top: 478px; }

  .brand { display: flex; align-items: center; gap: 14px; }
  .brand__dot {
    width: 56px; height: 56px; border-radius: 50%;
    background: var(--blue);
    flex: none;
  }
  .brand__name {
    font-weight: 700;
    font-size: 30px;
    color: var(--ink);
    letter-spacing: 0.5px;
    line-height: 1.1;
  }

  .card--logo .brand {
    position: absolute; left: 0; right: 0; top: 120px;
    justify-content: center;
  }
  .website {
    position: absolute; left: 0; right: 0; top: 222px;
    text-align: center;
    font-size: 16px;
    color: var(--ink);
  }
  .trim-bottom {
    position: absolute; left: 0; right: 0; bottom: 0;
    height: 16px;
    background: linear-gradient(var(--blue), var(--blue-deep));
  }

  .card--details .brand { position: absolute; left: 30px; top: 22px; gap: 10px; }
  .card--details .brand__dot { width: 40px; height: 40px; }
  .card--details .brand__name { font-size: 21px; }
  .trim-top {
    position: absolute; left: 30px; right: 30px; top: 82px;
    height: 5px; background: var(--blue);
  }
  .tagline {
    position: absolute; left: 200px; top: 94px;
    font-size: 12px; font-weight: 700; color: var(--grey);
    letter-spacing: 0.6px;
  }
  .channels { position: absolute; left: 30px; top: 102px; }
  .channels__row { display: flex; align-items: center; gap: 7px; margin-bottom: 6px; }
  .channels__circle { width: 18px; height: 18px; border-radius: 50%; background: var(--green); }
  .channels__label { font-size: 12px; font-weight: 700; color: var(--ink); }
  .channels__square { width: 20px; height: 20px; border-radius: 3px; background: var(--blue); }
  .channels__square--green { background: var(--green); border-radius: 50%; }

  .contact { position: absolute; left: 30px; top: 156px; list-style: none; }
  .contact li { display: flex; align-items: center; gap: 9px; font-size: 14px; line-height: 23px; white-space: nowrap; }
  .contact svg { width: 16px; height: 14px; flex: none; }

  .person {
    position: absolute; right: 36px; top: 220px;
    text-align: right; font-size: 14px; line-height: 20px;
  }
  .person__name { font-size: 26px; color: var(--blue); line-height: 32px; }

  .footer-bands { position: absolute; left: 0; bottom: 0; width: 660px; height: 20px; }
</style>
</head>
<body>

<section class="card card--logo" aria-label="Business card, brand side">
  <div class="brand">
    <span class="brand__dot"></span>
    <span class="brand__name">Brightpath HR Consulting</span>
  </div>
  <p class="website">www.brightpathhr-advisory.com</p>
  <div class="trim-bottom"></div>
</section>

<section class="card card--details" aria-label="Business card, contact side">
  <div class="brand">
    <span class="brand__dot"></span>
    <span class="brand__name">Brightpath HR Consulting</span>
  </div>
  <div class="trim-top"></div>
  <p class="tagline">Recruitment&nbsp; I &nbsp;HR Solutions&nbsp; I &nbsp;Business Consultancy</p>

  <div class="channels">
    <div class="channels__row">
      <span class="channels__circle"></span>
      <span class="channels__label">QuickChat</span>
    </div>
    <div class="channels__row">
      <span class="channels__square channels__square--green"></span>
      <span class="channels__square"></span>
      <span class="channels__square"></span>
    </div>
  </div>

  <ul class="contact">
    <li>
      <svg viewBox="0 0 16 14" aria-hidden="true"><rect x="4" y="0" width="8" height="14" rx="1.5" fill="none" stroke="#2a7fc9" stroke-width="1.5"/><line x1="7" y1="11.5" x2="9" y2="11.5" stroke="#2a7fc9" stroke-width="1.5"/></svg>
      (+65) 94386157
    </li>
    <li>
      <svg viewBox="0 0 16 14" aria-hidden="true"><rect x="0.5" y="2" width="15" height="10" fill="#2a7fc9"/><polyline points="0.5,2 8,8 15.5,2" fill="none" stroke="#fff" stroke-width="1.3"/></svg>
      mtellon@brightpathhr-advisory.com
    </li>
    <li>
      <svg viewBox="0 0 16 14" aria-hidden="true"><rect x="0.5" y="2" width="15" height="10" fill="#2a7fc9"/><polyline points="0.5,2 8,8 15.5,2" fill="none" stroke="#fff" stroke-width="1.3"/></svg>
      brightpathhradvisory@mailbox-example.com (alternative)
    </li>
  </ul>

  <div class="person">
    <p class="person__name">Marcus Tellon</p>
    <p>Business Development Director</p>
    <p>Brightpath HR Consulting Private Limited</p>
    <p>27 Wexford Lane, #05-03B</p>
    <p>Harbourview Trade Tower</p>
    <p>Singapore 061739</p>
  </div>

  <svg class="footer-bands" viewBox="0 0 660 20" preserveAspectRatio="none" aria-hidden="true">
    <defs>
      <linearGradient id="silverBand" x1="0" y1="0" x2="1" y2="0">
        <stop offset="0" stop-color="#bfc2c5"/>
        <stop offset="0.35" stop-color="#f2f2f2"/>
        <stop offset="0.7" stop-color="#7d8084"/>
        <stop offset="1" stop-color="#bfc2c5"/>
      </linearGradient>
    </defs>
    <polygon points="0,6 390,6 376,20 0,20" fill="url(#silverBand)"/>
    <polygon points="396,0 660,0 660,20 376,20" fill="#2a7fc9"/>
  </svg>
</section>

</body>
</html>
```